Company truck branding

I'm looking for a clean wrap design for my company vehicles and trailers. It needs to fit our branding based on logo. Most of our trucks and trailers are grey but we do have white trucks also. You can visit our website Parvetlandscaping.com or our instagram at parvetlandscaping

Industry/Entity Type

Landscaping

Font styles to use
Serif
Sans Serif

Colors

Designer to choose only greyscale colors for use in the design.

Requirements
Must have
• Want a Clean MODERN DESIGN
Should not have
• Don’t want grass or anything that is not on my logo.

```html
<!DOCTYPE html>
<html lang="en">
<head>
<meta charset="utf-8">
<title>Parvet Landscaping – Vehicle Wrap</title>
<link rel="stylesheet" href="https://fonts.googleapis.com/css2?family=Cinzel:wght@400;700&display=swap">
<style>
  :root {
    --ink: #1d1d1d;
    --paper: #ffffff;
    --stage: #efefef;
    --gold: #a58e6c;
    --tree: #5a5a5a;
    --muted: #e6e6e6;
  }
  * { margin: 0; padding: 0; box-sizing: border-box; }
  html, body { width: 1200px; height: 1200px; overflow: hidden; }
  body { background: var(--stage); font-family: "Cinzel", serif; color: var(--ink); position: relative; }

  .panel { position: absolute; background: var(--paper); overflow: hidden; box-shadow: 0 2px 10px rgba(0,0,0,.12); }
  .panel svg.shapes { position: absolute; inset: 0; width: 100%; height: 100%; }

  .trees { position: absolute; background: linear-gradient(180deg, rgba(90,90,90,0) 0%, rgba(90,90,90,.55) 45%, rgba(90,90,90,.75) 100%); }

  .brand-name { position: absolute; font-family: "Cinzel", serif; font-weight: 700; color: var(--ink); text-align: center; line-height: 1; }
  .brand-name .word { display: block; }
  .brand-name .sub { display: block; letter-spacing: .32em; margin-top: 8px; }

  .services { position: absolute; list-style: none; font-family: "Cinzel", serif; text-transform: uppercase; line-height: 1.35; }
  .services li { position: relative; padding-left: 14px; }
  .services li::before { content: ""; position: absolute; left: 0; top: .45em; width: 6px; height: 6px; border-radius: 50%; background: var(--gold); }

  .contact { position: absolute; color: var(--paper); font-family: "Cinzel", serif; text-align: center; }
  .contact .phone { display: block; line-height: 1.1; }
  .contact .web { display: block; letter-spacing: .02em; }

  /* side wrap */
  .side-wrap { left: 40px; top: 110px; width: 1120px; height: 440px; }
  .side-wrap .trees { left: 700px; top: 130px; width: 420px; height: 310px; }
  .side-wrap .brand-name { left: 80px; top: 135px; width: 330px; }
  .side-wrap .brand-name .word { font-size: 66px; }
  .side-wrap .brand-name .sub { font-size: 19px; }
  .side-wrap .services { left: 440px; top: 150px; font-size: 15px; color: var(--ink); }
  .side-wrap .contact { left: 740px; top: 38px; width: 360px; }
  .side-wrap .contact .phone { font-size: 44px; }
  .side-wrap .contact .web { font-size: 20px; }

  /* hood decal */
  .hood-decal { left: 40px; top: 640px; width: 540px; height: 460px; }
  .hood-decal .brand-name { left: 0; top: 180px; width: 540px; }
  .hood-decal .brand-name .word { font-size: 72px; }
  .hood-decal .brand-name .sub { font-size: 22px; }

  /* tailgate */
  .tailgate { left: 620px; top: 700px; width: 540px; height: 340px; }
  .tailgate .trees { left: 300px; top: 60px; width: 240px; height: 280px; }
  .tailgate .brand-name { left: 20px; top: 120px; width: 250px; }
  .tailgate .brand-name .word { font-size: 50px; }
  .tailgate .brand-name .sub { font-size: 14px; }
  .tailgate .services { left: 345px; top: 60px; font-size: 12px; color: var(--paper); }
  .tailgate .contact { left: 290px; top: 200px; width: 240px; }
  .tailgate .contact .phone { font-size: 32px; }
  .tailgate .contact .web { font-size: 15px; }
</style>
</head>
<body>

<section class="panel side-wrap" aria-label="Side wrap">
  <svg class="shapes" viewBox="0 0 1120 440" aria-hidden="true">
    <polygon points="745,0 1120,0 1120,440 470,440 540,372 690,372" fill="var(--ink)"/>
    <polyline points="718,0 660,346 520,346 425,440" fill="none" stroke="var(--gold)" stroke-width="5"/>
  </svg>
  <div class="trees" role="img" aria-label="Grey pine forest silhouette"></div>
  <div class="brand-name"><span class="word">PARVET</span><span class="sub">LANDSCAPING</span></div>
  <ul class="services">
    <li>Plant Healthcare</li>
    <li>Landscape Maintenance</li>
    <li>Hardscapes</li>
    <li>Design Build</li>
  </ul>
  <div class="contact">
    <span class="phone">123-456-7890</span>
    <span class="web">PARVETLANDSCAPING.COM</span>
  </div>
</section>

<section class="panel hood-decal" aria-label="Hood decal">
  <div class="brand-name"><span class="word">PARVET</span><span class="sub">LANDSCAPING</span></div>
</section>

<section class="panel tailgate" aria-label="Tailgate wrap">
  <svg class="shapes" viewBox="0 0 540 340" aria-hidden="true">
    <polygon points="290,0 540,0 540,340 200,340 290,250" fill="var(--ink)"/>
  </svg>
  <div class="trees" role="img" aria-label="Grey pine forest silhouette"></div>
  <div class="brand-name"><span class="word">PARVET</span><span class="sub">LANDSCAPING</span></div>
  <ul class="services">
    <li>Plant Healthcare</li>
    <li>Landscape Maintenance</li>
    <li>Hardscapes</li>
    <li>Design Build</li>
  </ul>
  <div class="contact">
    <span class="phone">123-456-7890</span>
    <span class="web">PARVETLANDSCAPING.COM</span>
  </div>
</section>

</body>
</html>
```